ALL ASPECTS OF PLASTERING INC: TEXTURE,SANDFINISH RENO,POOLS, PATCH WORK ( STATEWIDE SERVICE GOOD RATES) 100% GUARANTEED FULLY INSURED C

Target Market(s)

ANYONE WHO OWNS A HOUSE,BUILDERS

Industry/Entity Type

Work

Contact Information for Business Card

STONEVALE PLASTERING SERVICES
GERALD PETRAKIS 0438916247
EMAIL:VORTAKE58@QUENMAIL.COM

Requirements
Must have
• COLOUR BACKGROUND WIV PLASTERING PICTURE EG TROWEL, CEMENT MIXER, SAND
Nice to have
• BOLD PROFESSIONAL LOOKING AND SOUNDING CATCHY SAYING
Should not have
• FLURO COLOURS

```html
<!DOCTYPE html>
<html lang="en">
<head>
<meta charset="utf-8">
<title>Stonevale Plastering Services – Business Card</title>
<link href="https://fonts.googleapis.com/css2?family=Alfa+Slab+One&family=Mulish:wght@400;700;800&family=Open+Sans:wght@700&display=swap" rel="stylesheet">
<style>
  :root {
    --page-bg: #ebecec;
    --charcoal: #2b2a29;
    --orange: #ee7322;
    --white: #ffffff;
    --ink: #2b2a29;
    --mixer-orange: #f07a2a;
    --mixer-shade: #c75a16;
    --figure-light: #f2f2f2;
    --figure-mid: #bdbdbd;
  }
  * { box-sizing: border-box; margin: 0; padding: 0; }
  html, body {
    width: 965px; height: 1200px; overflow: hidden;
    background: var(--page-bg);
  }
  .canvas { position: relative; width: 965px; height: 1200px; }

  .card {
    position: absolute;
    width: 722px; height: 452px;
    border-radius: 30px;
    overflow: hidden;
    background: var(--white);
    box-shadow: 0 6px 18px rgba(0,0,0,0.14);
  }
  .card--front { left: 123px; top: 82px; }
  .card--back  { left: 128px; top: 637px; }

  .band-dark { position: absolute; left: 0; width: 100%; background: var(--charcoal); }
  .band-accent { position: absolute; left: 0; width: 100%; height: 11px; background: var(--orange); }

  .brand-name {
    position: absolute;
    font-family: "Mulish", Arial, sans-serif;
    font-weight: 800;
    color: var(--orange);
    letter-spacing: 1px;
    white-space: nowrap;
    line-height: 1;
  }
  .brand-service {
    position: absolute;
    font-family: "Alfa Slab One", Georgia, serif;
    letter-spacing: 0.5px;
    white-space: nowrap;
    line-height: 1;
  }

  /* Front */
  .card--front .band-dark { top: 0; height: 261px; }
  .card--front .band-accent { top: 261px; }
  .card--front .brand-name { left: 194px; top: 73px; font-size: 35px; }
  .card--front .brand-service { left: 80px; top: 163px; font-size: 33px; color: var(--white); }
  .worker-art {
    position: absolute; left: 575px; top: 25px; width: 140px; height: 236px;
    background: linear-gradient(160deg, var(--figure-light) 0%, var(--figure-mid) 100%);
    border-radius: 60px 60px 0 0;
    opacity: 0.9;
  }

  .contact {
    position: absolute; left: 0; width: 100%;
    text-align: center; color: var(--ink);
  }
  .contact-name {
    top: 307px;
    font-family: "Open Sans", Arial, sans-serif;
    font-weight: 700; font-size: 23px; letter-spacing: 0.3px;
  }
  .contact-line {
    font-family: "Mulish", Arial, sans-serif;
    font-size: 25px; font-weight: 400;
    display: flex; justify-content: center; align-items: center; gap: 8px;
  }
  .contact-phone { top: 350px; }
  .contact-email { top: 390px; }
  .contact-line svg { flex: none; }

  /* Back */
  .card--back .band-dark { top: 216px; height: 236px; }
  .card--back .band-accent { top: 203px; height: 13px; }
  .mixer-art {
    position: absolute; left: 27px; top: 21px; width: 230px; height: 179px;
    background: radial-gradient(ellipse at 65% 40%, var(--mixer-orange) 0%, var(--mixer-shade) 55%, #ffffff 80%);
  }
  .card--back .brand-name { left: 0; width: 100%; padding-left: 188px; text-align: center; top: 80px; font-size: 31px; }
  .card--back .brand-service { left: 0; width: 100%; padding-left: 188px; text-align: center; top: 132px; font-size: 23.5px; color: var(--ink); }

  .services-heading {
    position: absolute; left: 157px; top: 232px;
    font-family: "Mulish", Arial, sans-serif;
    font-weight: 700; font-size: 24px; color: var(--orange);
  }
  .services-list {
    position: absolute; left: 164px; top: 270px;
    list-style: none;
    font-family: "Mulish", Arial, sans-serif;
    font-size: 23.5px; color: var(--white);
  }
  .services-list li {
    position: relative; padding-left: 27px;
    height: 28.8px; line-height: 28.8px; white-space: nowrap;
  }
  .services-list li::before {
    content: ""; position: absolute; left: 2px; top: 10px;
    width: 8px; height: 8px; background: var(--white);
    transform: rotate(45deg);
  }
  .services-list strong { font-weight: 800; }
</style>
</head>
<body>
<main class="canvas">

  <section class="card card--front" aria-label="Business card front">
    <div class="band-dark"></div>
    <div class="band-accent"></div>
    <div class="worker-art" role="img" aria-label="Illustration of a plasterer in cap and apron applying plaster with a trowel"></div>
    <h1 class="brand-name">STONEVALE</h1>
    <p class="brand-service">PLASTERING SERVICES</p>

    <p class="contact contact-name">GERALD PETRAKIS</p>
    <p class="contact contact-line contact-phone">
      <svg width="20" height="20" viewBox="0 0 24 24" aria-hidden="true"><path d="M6.6 10.8a15.1 15.1 0 0 0 6.6 6.6l2.2-2.2c.3-.3.7-.4 1-.2 1.1.4 2.3.6 3.6.6.6 0 1 .4 1 1V20c0 .6-.4 1-1 1A17 17 0 0 1 3 4c0-.6.4-1 1-1h3.5c.6 0 1 .4 1 1 0 1.3.2 2.5.6 3.6.1.3 0 .7-.2 1z" fill="none" stroke="#2b2a29" stroke-width="1.8"/></svg>
      <span>0438916247</span>
    </p>
    <p class="contact contact-line contact-email">
      <svg width="24" height="18" viewBox="0 0 24 18" aria-hidden="true"><rect x="1" y="1" width="22" height="16" fill="none" stroke="#2b2a29" stroke-width="1.8"/><path d="M1 1l11 9 11-9M1 17l8-7M23 17l-8-7" fill="none" stroke="#2b2a29" stroke-width="1.6"/></svg>
      <span>vortake58@quenmail.com</span>
    </p>
  </section>

  <section class="card card--back" aria-label="Business card back">
    <div class="mixer-art" role="img" aria-label="Photo of an orange portable cement mixer on wheels"></div>
    <h2 class="brand-name">STONEVALE</h2>
    <p class="brand-service">PLASTERING SERVICES</p>
    <div class="band-accent"></div>
    <div class="band-dark"></div>

    <p class="services-heading">All aspects of plastering:</p>
    <ul class="services-list">
      <li><strong>Texture</strong></li>
      <li><strong>Sandfinish reno</strong></li>
      <li><strong>Pools</strong></li>
      <li><strong>Patch work</strong> (statewide service good rates)</li>
      <li><strong>100% guaranteed fully insured</strong></li>
    </ul>
  </section>

</main>
</body>
</html>
```